Dunmore Air & Co business card

I need an awesome, double-sided business card designed with our new logo. I would like the one side black with the colored logo, and the back side is all yours. I'd like to see horizontal and vertical layouts. Get creative! Thank you.

Target Market(s)

HVAC, Heating and Cooling in Phoenix, AZ

Industry/Entity Type

HVAC

Contact Information for Business Card

We need our new logo on the card. Tom Harker, (623) 417-2958, tom@brightvaleair.com, www.brightvaleair.com, ROC 581427

```html
<!DOCTYPE html>
<html lang="en">
<head>
<meta charset="utf-8">
<title>Dunmore Air &amp; Co — Business Card</title>
<link href="https://fonts.googleapis.com/css2?family=Montserrat:wght@400;500;600;800&display=swap" rel="stylesheet">
<style>
  :root {
    --page-bg: #e9eaec;
    --card-black: #1f1f20;
    --card-black-edge: #2b2b2c;
    --emboss: #3a3a3c;
    --brand-blue: #0b6fc2;
    --brand-blue-dark: #0a5ea6;
    --brand-orange: #f07a1e;
    --ink: #2a2a2a;
    --white: #ffffff;
  }
  * { margin: 0; padding: 0; box-sizing: border-box; }
  html, body { width: 1200px; height: 900px; overflow: hidden; }
  body {
    background: var(--page-bg);
    font-family: "Montserrat", sans-serif;
    position: relative;
  }
  .card {
    position: absolute;
    left: 250px;
    width: 700px;
    height: 400px;
    overflow: hidden;
    box-shadow: 0 10px 28px rgba(0,0,0,0.18);
  }
  /* Front side */
  .card-front {
    top: 35px;
    background: linear-gradient(135deg, var(--card-black-edge), var(--card-black));
    display: flex;
    align-items: center;
    justify-content: center;
  }
  .front-wordmark {
    display: flex;
    align-items: center;
    gap: 18px;
    color: var(--emboss);
    font-weight: 800;
    font-size: 44px;
    letter-spacing: 1px;
  }
  .front-wordmark .mark-dot {
    width: 34px; height: 34px; border-radius: 50%;
    background: var(--emboss);
  }
  /* Back side */
  .card-back {
    top: 465px;
    background: var(--white);
  }
  .name-band {
    position: absolute;
    left: 0; top: 34px;
    width: 100%; height: 118px;
    background: var(--brand-blue);
  }
  .holder-name {
    position: absolute;
    left: 60px; top: 64px;
    color: var(--white);
    font-weight: 800;
    font-size: 26px;
    letter-spacing: 1.5px;
    text-transform: uppercase;
  }
  .holder-title {
    position: absolute;
    left: 60px; top: 98px;
    color: var(--white);
    font-weight: 400;
    font-size: 17px;
  }
  .logo-plate {
    position: absolute;
    right: 30px; top: 96px;
    width: 270px; height: 132px;
    background: var(--white);
    border-radius: 18px;
    display: flex;
    align-items: center;
    justify-content: center;
    gap: 12px;
  }
  .logo-plate .wordmark {
    color: var(--brand-blue);
    font-weight: 800;
    font-size: 25px;
  }
  .logo-plate .mark-dot {
    width: 22px; height: 22px; border-radius: 50%;
    background: var(--brand-blue);
  }
  .contact-block {
    position: absolute;
    left: 60px; top: 184px;
    color: var(--ink);
  }
  .licence {
    color: var(--brand-blue);
    font-weight: 600;
    font-size: 17px;
    margin-bottom: 2px;
  }
  .address { font-size: 17px; line-height: 1.35; }
  .contact-list { list-style: none; margin-top: 16px; }
  .contact-list li {
    display: flex; align-items: center; gap: 10px;
    font-size: 17px; line-height: 1.45;
  }
  .contact-list svg { width: 14px; height: 14px; flex: none; }
  .bottom-stripe {
    position: absolute;
    left: 0; bottom: 12px;
    width: 100%; height: 10px;
    background: var(--brand-blue);
  }
  .corner-decoration {
    position: absolute;
    right: 0; bottom: 0;
    width: 190px; height: 150px;
    border-top-left-radius: 160px 140px;
    background: linear-gradient(160deg, var(--brand-blue), var(--brand-blue-dark));
  }
</style>
</head>
<body>

  <section class="card card-front">
    <div class="front-wordmark">
      <span class="mark-dot"></span>
      <span>Dunmore Air &amp; Co</span>
    </div>
  </section>

  <section class="card card-back">
    <div class="name-band"></div>
    <div class="holder-name">Tom Harker</div>
    <div class="holder-title">Director</div>

    <div class="logo-plate">
      <span class="mark-dot"></span>
      <span class="wordmark">Dunmore Air &amp; Co</span>
    </div>

    <div class="contact-block">
      <p class="licence">ROC 581427</p>
      <p class="address">2406 Saguaro Bend<br>Glendale, AZ 85301</p>
      <ul class="contact-list">
        <li>
          <svg viewBox="0 0 24 24" aria-hidden="true"><path fill="#f07a1e" d="M6.6 10.8a15 15 0 0 0 6.6 6.6l2.2-2.2a1 1 0 0 1 1-.25 11.4 11.4 0 0 0 3.6.57 1 1 0 0 1 1 1V20a1 1 0 0 1-1 1A17 17 0 0 1 3 4a1 1 0 0 1 1-1h3.5a1 1 0 0 1 1 1c0 1.25.2 2.45.57 3.57a1 1 0 0 1-.25 1z"/></svg>
          (623) 417-2958
        </li>
        <li>
          <svg viewBox="0 0 24 24" aria-hidden="true"><rect x="2.5" y="5" width="19" height="14" rx="1.5" fill="none" stroke="#f07a1e" stroke-width="2"/><path d="M3 6l9 7 9-7" fill="none" stroke="#f07a1e" stroke-width="2"/></svg>
          tom@brightvaleair.com
        </li>
        <li>
          <svg viewBox="0 0 24 24" aria-hidden="true"><g fill="none" stroke="#f07a1e" stroke-width="2"><circle cx="12" cy="12" r="9.5"/><ellipse cx="12" cy="12" rx="4" ry="9.5"/><path d="M2.5 12h19M4 7h16M4 17h16"/></g></svg>
          www.brightvaleair.com
        </li>
      </ul>
    </div>

    <div class="bottom-stripe"></div>
    <div class="corner-decoration" role="img" aria-label="Large cropped brand emblem in blue as corner decoration"></div>
  </section>

</body>
</html>
```